Cedar Hollow Business Card and Logo

Nutrition and Wellness Store Front. I sell supplements, herbs, tinctures, Loose Leaf Teas, natural snacks and drinks including gluten free. classes: Fitness; health and wellness; community health and wellness hub. It is a "shabby chic" store front. It is white and my accent color is turqouise I will be adding some jewelry, stones and rocks and jewelery. I am a Certified Herbalist and Certified Nutrition and Wellness Consultant, a Solvane Practitioner and Kavora instructor.

Target Market(s)

health and wellness seekers, fitness, baby boomer

Industry/Entity Type

Business

Contact Information for Business Card

Cedar Hollow Nutrition and Wellness
Marla Dunstable Certified Herbalist , Certified Nutrition and Wellness Consultant, Solvane Practitioner, Kavora Instructor

Font styles to use
Serif

Colors
33a6d7
3176b5
33b8a4

Requirements
Must have
• A picture that represents two mountain peaks with a floral accent.

```html
<!DOCTYPE html>
<html lang="en">
<head>
<meta charset="utf-8">
<title>Cedar Hollow Nutrition and Wellness – Business Card</title>
<link href="https://fonts.googleapis.com/css2?family=Open+Sans:wght@300;400;700&display=swap" rel="stylesheet">
<style>
  :root {
    --page-bg: #e9e6e1;
    --card-white: #ffffff;
    --deep-blue: #3176b5;
    --sky-blue: #33a6d7;
    --teal: #33b8a4;
    --soft-grey: #8f979d;
    --text-grey: #6c757b;
  }
  html, body {
    margin: 0;
    padding: 0;
    width: 1200px;
    height: 1022px;
    overflow: hidden;
    background: var(--page-bg);
    font-family: "Open Sans", Arial, sans-serif;
  }
  .card {
    position: absolute;
    left: 100px;
    top: 226px;
    width: 1000px;
    height: 570px;
    border-radius: 18px;
    overflow: hidden;
    box-shadow: 0 10px 30px rgba(0,0,0,0.18);
    background: var(--card-white);
  }
  .card__landscape {
    position: absolute;
    inset: 0;
    background: linear-gradient(180deg,
      #f1f3f5 0%, #d5dce2 30%, #a7b2bc 50%, #8794a0 60%,
      #86a85a 70%, #a195d0 82%, #7ba04c 100%);
  }
  .card__panel {
    position: absolute;
    inset: 0;
  }
  .brand {
    position: absolute;
    left: 470px;
    top: 46px;
    display: flex;
    flex-direction: column;
    align-items: flex-start;
  }
  .brand__mark {
    width: 62px;
    height: 62px;
    border-radius: 50%;
    border: 3px solid var(--sky-blue);
    box-sizing: border-box;
    margin-left: 50px;
    margin-bottom: 14px;
  }
  .brand__name {
    font-weight: 300;
    font-size: 34px;
    line-height: 42px;
    color: var(--soft-grey);
    letter-spacing: 0.5px;
  }
  .brand__name span { display: block; padding-left: 90px; }
  .person {
    position: absolute;
    left: 370px;
    top: 240px;
    width: 560px;
  }
  .person__name {
    font-weight: 700;
    font-size: 52px;
    line-height: 60px;
    color: var(--deep-blue);
  }
  .person__title {
    text-align: right;
    font-size: 30px;
    line-height: 36px;
    color: var(--sky-blue);
    padding-right: 20px;
  }
  .credentials {
    position: absolute;
    right: 40px;
    top: 372px;
    text-align: right;
  }
  .credential {
    font-size: 29px;
    line-height: 42px;
    color: var(--text-grey);
    white-space: nowrap;
  }
  .credential--wide {
    position: absolute;
    left: 230px;
    top: 498px;
    white-space: nowrap;
  }
  .tick {
    display: inline-block;
    width: 22px;
    height: 18px;
    margin-left: 8px;
    vertical-align: middle;
  }
</style>
</head>
<body>
  <div class="card">
    <div class="card__landscape" role="img" aria-label="Photo of two mountain peaks in mist above a meadow of purple lupines and white wildflowers"></div>

    <svg class="card__panel" width="1000" height="570" viewBox="0 0 1000 570">
      <defs>
        <linearGradient id="edgeBlue" x1="0" y1="0" x2="0" y2="1">
          <stop offset="0" stop-color="#33a6d7"/>
          <stop offset="1" stop-color="#3176b5"/>
        </linearGradient>
      </defs>
      <path d="M362,0 C214,170 186,390 214,570 L1000,570 L1000,0 Z" fill="url(#edgeBlue)"/>
      <path d="M380,0 C232,170 204,390 232,570 L1000,570 L1000,0 Z" fill="#ffffff"/>
    </svg>

    <div class="brand">
      <div class="brand__mark"></div>
      <div class="brand__name">Cedar Hollow Nutrition<span>and Wellness</span></div>
    </div>

    <div class="person">
      <div class="person__name">Marla Dunstable</div>
      <div class="person__title">Certified Herbalist</div>
    </div>

    <div class="credentials">
      <div class="credential">Solvane Practitioner<svg class="tick" viewBox="0 0 22 18"><path d="M2,9 L8,15 L20,3" fill="none" stroke="#33a6d7" stroke-width="3.5" stroke-linecap="round" stroke-linejoin="round"/></svg></div>
      <div class="credential">Kavora Instructor<svg class="tick" viewBox="0 0 22 18"><path d="M2,9 L8,15 L20,3" fill="none" stroke="#33a6d7" stroke-width="3.5" stroke-linecap="round" stroke-linejoin="round"/></svg></div>
    </div>

    <div class="credential credential--wide">Certified Nutrition and Wellness Consultant<svg class="tick" viewBox="0 0 22 18"><path d="M2,9 L8,15 L20,3" fill="none" stroke="#33a6d7" stroke-width="3.5" stroke-linecap="round" stroke-linejoin="round"/></svg></div>
  </div>
</body>
</html>
```